Residential Construction Business - Site Signage

I need a design made for a site fence banner. We have a logo and branding so the design would need to be aligned with this. It would need to be made to specific size ratio so that it can be sent to the maker for production.
ratio : 4600 wide x 1700 high
The design should feature our website and also the slogan
"don't move, re-imagine"

Target Market(s)

potential clients

Industry/Entity Type

construction

Font styles to use
Other font styles liked:
• to match branding

Colors
0054AA
0677BA
7BADD7
CADEEF
E8F1F8

Requirements
Must have
• www.velmbuild.com.au Majority of the sign is our brand logo
Nice to have
• Majority of the sign is our brand logo
Should not have
• colors and themes that arent brand relevant

```html
<!DOCTYPE html>
<html lang="en">
<head>
<meta charset="utf-8">
<title>Velm Build – Site Fence Banner</title>
<link rel="stylesheet" href="https://fonts.googleapis.com/css2?family=Lato:wght@400;700&display=swap">
<style>
  :root {
    --navy: #22415f;
    --panel: #f4f4f5;
    --backdrop: #e4e4e4;
  }
  * { margin: 0; padding: 0; box-sizing: border-box; }
  html, body {
    width: 1200px;
    height: 715px;
    overflow: hidden;
    background: var(--backdrop);
  }
  .banner {
    position: absolute;
    left: 20px;
    top: 143px;
    width: 1160px;
    height: 429px;
    background: var(--panel);
    overflow: hidden;
  }
  .banner__chevron {
    position: absolute;
    inset: 0;
    width: 100%;
    height: 100%;
  }
  .banner__chevron polygon { fill: var(--navy); }
  .brand-name {
    position: absolute;
    left: 430px;
    top: 184px;
    font-family: "Lato", sans-serif;
    font-weight: 700;
    font-size: 56px;
    line-height: 56px;
    letter-spacing: 0;
    color: var(--navy);
    white-space: nowrap;
  }
  .divider {
    position: absolute;
    left: 852px;
    top: 120px;
    width: 2px;
    height: 190px;
    background: var(--navy);
  }
  .tagline {
    position: absolute;
    left: 871px;
    top: 148px;
    font-family: "Lato", sans-serif;
    font-weight: 700;
    font-size: 38px;
    line-height: 42px;
    color: var(--navy);
    white-space: nowrap;
  }
  .website {
    position: absolute;
    left: 872px;
    top: 258px;
    font-family: "Lato", sans-serif;
    font-weight: 400;
    font-size: 23px;
    line-height: 1;
    letter-spacing: 0.3px;
    color: var(--navy);
    white-space: nowrap;
  }
</style>
</head>
<body>
  <main class="banner">
    <svg class="banner__chevron" viewBox="0 0 1160 429" preserveAspectRatio="none" aria-hidden="true">
      <polygon points="0,0 528,0 355,214 544,429 0,429"/>
    </svg>
    <div class="brand-name">Velm Build</div>
    <div class="divider"></div>
    <p class="tagline">DON’T MOVE,<br>RE-IMAGINE</p>
    <p class="website">VELMBUILD.COM.AU</p>
  </main>
</body>
</html>
```